Harborline Security and Surveillance Business Card

Business Card Design - Company Name:Freedom Security and SurveillanceWe are a Security Systems Integrator Specializing in Security Systems/ Video Surveillance and Access Control. Our areas of expertise are:Security SystemsVideo SurveillanceAccess ControlFire Alarm SystemsNetwork CablingCellular BoostersMy input is the Front of the Card is: logo, name of Business, My Name, Phone Number, and email.Rear of Card is the 6 areas of expertise, I just dont want the front to be very busy.
Name: Tom Werner
Title: President
Email: tom@harborlinesecsys.example
website: harborlinesecsys.example

```html
<!DOCTYPE html>
<html lang="en">
<head>
<meta charset="utf-8">
<title>Harborline Security and Surveillance — Business Card</title>
<link rel="stylesheet" href="https://fonts.googleapis.com/css2?family=Lato:wght@700&family=Open+Sans:wght@400;600;700&display=swap">
<style>
  :root {
    --brand-blue: #255eaa;
    --ink-grey: #5f5f5f;
    --rule-grey: #7a7a7a;
    --paper: #ffffff;
    --backdrop: #e4e4e4;
  }
  * { margin: 0; padding: 0; box-sizing: border-box; }
  html, body { width: 1200px; height: 800px; overflow: hidden; }
  body { background: var(--backdrop); font-family: "Open Sans", sans-serif; position: relative; }

  .card { position: absolute; width: 557px; height: 327px; }
  .card--front { left: 322px; top: 68px; background: var(--brand-blue); color: var(--paper); }
  .card--back { left: 322px; top: 434px; background: var(--paper); }

  .wordmark { font-family: "Open Sans", sans-serif; font-weight: 600; text-transform: uppercase; text-align: center; }
  .card--front .wordmark-mark {
    position: absolute; left: 50%; top: 50px; width: 40px; height: 40px;
    margin-left: -20px; border-radius: 50%; background: var(--paper);
  }
  .card--front .wordmark {
    position: absolute; left: 0; right: 0; top: 108px; color: var(--paper);
    font-size: 25px; letter-spacing: 3px; line-height: 1.1;
  }
  .card--front .wordmark small { display: block; font-size: 10px; letter-spacing: 3px; font-weight: 600; }

  .services {
    position: absolute; left: 0; right: 0; top: 228px;
    font-family: "Lato", sans-serif; font-weight: 700; font-size: 15.5px;
    letter-spacing: 0.6px; line-height: 24px; text-align: center;
  }

  .card--back .wordmark-block { position: absolute; left: 38px; top: 50px; width: 214px; }
  .card--back .wordmark-mark {
    display: block; width: 34px; height: 34px; margin: 0 auto 8px;
    border-radius: 50%; background: var(--brand-blue);
  }
  .card--back .wordmark { color: var(--brand-blue); font-size: 16px; letter-spacing: 1.5px; line-height: 1.15; }
  .card--back .wordmark small { display: block; font-size: 7.5px; letter-spacing: 2px; font-weight: 600; }

  .person { position: absolute; right: 45px; top: 150px; text-align: right; }
  .person-name { color: var(--brand-blue); font-weight: 700; font-size: 21px; line-height: 1.2; text-transform: uppercase; }
  .person-title { color: var(--ink-grey); font-size: 15px; line-height: 1.3; }

  .divider { position: absolute; left: 38px; right: 45px; top: 199px; height: 2px; background: var(--rule-grey); }

  .contacts { position: absolute; left: 38px; top: 214px; list-style: none; }
  .contacts li { display: flex; align-items: center; height: 21.5px; color: var(--ink-grey); font-size: 14px; }
  .contacts svg { width: 16px; height: 16px; margin-right: 7px; fill: var(--brand-blue); flex: none; }
</style>
</head>
<body>
  <section class="card card--front" aria-label="Card front">
    <span class="wordmark-mark" aria-hidden="true"></span>
    <h1 class="wordmark">Harborline Security<small>and Surveillance</small></h1>
    <p class="services">
      Security Systems | Video Surveillance | Access Control<br>
      Fire Alarm Systems | Network Cabling | Cellular Boosters
    </p>
  </section>

  <section class="card card--back" aria-label="Card back">
    <div class="wordmark-block">
      <span class="wordmark-mark" aria-hidden="true"></span>
      <h2 class="wordmark">Harborline Security<small>and Surveillance</small></h2>
    </div>

    <div class="person">
      <p class="person-name">Tom Werner</p>
      <p class="person-title">President</p>
    </div>

    <div class="divider"></div>

    <ul class="contacts">
      <li>
        <svg viewBox="0 0 16 16" aria-hidden="true"><path d="M4 0h8a1 1 0 0 1 1 1v14a1 1 0 0 1-1 1H4a1 1 0 0 1-1-1V1a1 1 0 0 1 1-1zm.6 1.6v10.8h6.8V1.6zM8 13.2a.9.9 0 1 0 0 1.8.9.9 0 0 0 0-1.8z"/></svg>
        (555) 014-2290
      </li>
      <li>
        <svg viewBox="0 0 16 16" aria-hidden="true"><path d="M0 3h16v10H0zm1.6 1.3L8 9l6.4-4.7v-.1H1.6zm0 1.7v5.8h12.8V6L8 10.6z"/></svg>
        tom@harborlinesecsys.example
      </li>
      <li>
        <svg viewBox="0 0 16 16" aria-hidden="true"><path d="M8 0a8 8 0 1 1 0 16A8 8 0 0 1 8 0zm0 1.4a6.6 6.6 0 0 0-5.8 3.4h11.6A6.6 6.6 0 0 0 8 1.4zM1.8 6.3v3.4h12.4V6.3zm.4 4.9a6.6 6.6 0 0 0 11.6 0z"/></svg>
        harborlinesecsys.example
      </li>
      <li>
        <svg viewBox="0 0 16 16" aria-hidden="true"><path d="M8 0a5.5 5.5 0 0 1 5.5 5.5C13.5 9.6 8 16 8 16S2.5 9.6 2.5 5.5A5.5 5.5 0 0 1 8 0zm0 3.3a2.2 2.2 0 1 0 0 4.4 2.2 2.2 0 0 0 0-4.4z"/></svg>
        Port Aldwin, Minnesota 55990, United States
      </li>
    </ul>
  </section>
</body>
</html>
```